New Solo Law Office Needs Business Card/Letterhead Design

I am starting a solo law office called "Law Office of Brian Kolmer, PLLC" in Tucson, Arizona. I will be doing criminal defense trial work. More than a logo with any sort of icon, I am really just looking for the name of the company to be displayed in a sleek, minimalist but interesting sort of way, with a format and font type that communicates professionalism. It can be in color, but doesn't have to be, and I am thinking blue and/or red accents colors. I'd like it to convey that I am passionate, dependable and willing to fight. For the business card, I envision sort of higher quality card material, and maybe some embossing or raised print. I will want to include my company name, name, phone and fax numbers, email and website addresses. For the letterhead, I will want to be able to use the same sort of font/formatting design as on the business card.
Industry/Entity Type
Business
Contact Information for Business Card
Law Office of Brian Kolmer, PLLC
Brian Kolmer
brian@kolmer-law.example
www.kolmer-law.example
(I do not yet have an established phone or fax number, so please put in some place holder numbers for the formatting, and I can add the actual numbers in before I print.)
Colors
Designer to choose colors to be used in the design.
Look and feel
Each slider illustrates characteristics of the customer's brand and the style your logo design should communicate.

```html
<!DOCTYPE html>
<html lang="en">
<head>
<meta charset="utf-8">
<title>Law Office of Brian Kolmer, PLLC — Stationery</title>
<link rel="stylesheet" href="https://fonts.googleapis.com/css2?family=Cinzel:wght@400;600&family=Arimo:wght@400&display=swap">
<style>
  :root {
    --burgundy: #7a1419;
    --burgundy-deep: #5a0d11;
    --charcoal: #3a3a3a;
    --ink: #222222;
    --muted: #6b6b6b;
    --paper: #ffffff;
    --backdrop: #ececec;
    --display: "Cinzel", "Times New Roman", serif;
    --body: "Arimo", Arial, sans-serif;
  }
  * { box-sizing: border-box; margin: 0; padding: 0; }
  html, body { width: 1200px; height: 1000px; overflow: hidden; }
  body { background: var(--backdrop); position: relative; font-family: var(--body); color: var(--ink); }

  /* ---------- Letterhead ---------- */
  .letterhead {
    position: absolute; left: 50px; top: 50px; width: 680px; height: 880px;
    background: var(--paper); box-shadow: 0 4px 18px rgba(0,0,0,.12);
  }
  .letterhead__rule-red { position: absolute; left: 0; top: 0; width: 62%; height: 6px; background: var(--burgundy); }
  .letterhead__rule-dark { position: absolute; right: 0; top: 0; width: 37%; height: 10px; background: var(--charcoal); }
  .brand { position: absolute; display: flex; align-items: center; gap: 10px; }
  .letterhead .brand { left: 48px; top: 52px; }
  .brand__mark { width: 40px; height: 40px; background: var(--burgundy); flex: none; }
  .brand__name {
    font-family: var(--display); font-weight: 400; color: var(--burgundy);
    text-transform: uppercase; line-height: 1.05; letter-spacing: .02em;
  }
  .letterhead .brand__name { font-size: 17px; }
  .letterhead__contact {
    position: absolute; right: 48px; top: 24px; text-align: left;
    font-family: var(--display); font-size: 9px; line-height: 1.55; color: var(--burgundy);
    letter-spacing: .04em;
  }
  .letterhead__body { position: absolute; left: 48px; top: 170px; width: 584px; font-size: 12px; line-height: 1.55; }
  .recipient { margin-bottom: 26px; }
  .salutation { margin-bottom: 12px; }
  .letterhead__body p.paragraph { margin-bottom: 12px; text-align: justify; }
  .signature { width: 90px; height: 48px; background: linear-gradient(135deg, #e6e6e6, #cfcfcf); margin-top: 30px; margin-bottom: 6px; border-radius: 4px; }

  /* ---------- Business cards ---------- */
  .card {
    position: absolute; left: 760px; width: 400px; height: 230px;
    background: var(--paper); box-shadow: 0 4px 14px rgba(0,0,0,.14);
    border-top: 9px solid var(--burgundy-deep); border-bottom: 9px solid var(--burgundy-deep);
  }
  .card--upper { top: 170px; }
  .card--lower { top: 560px; }
  .card .brand { left: 28px; top: 26px; }
  .card .brand__mark { width: 32px; height: 32px; }
  .card .brand__name { font-size: 14px; }
  .card__rule { position: absolute; left: 28px; right: 28px; top: 100px; height: 1px; background: var(--burgundy); }
  .card__details { position: absolute; left: 28px; right: 28px; top: 112px; font-family: var(--display); }
  .card__title { font-size: 13px; color: var(--burgundy); letter-spacing: .03em; white-space: nowrap; }
  .card__title .role { color: var(--muted); font-size: 11px; }
  .card__line { font-size: 9px; color: var(--muted); letter-spacing: .03em; margin-top: 5px; white-space: nowrap; }
</style>
</head>
<body>

<article class="letterhead">
  <div class="letterhead__rule-red"></div>
  <div class="letterhead__rule-dark"></div>

  <div class="letterhead__contact">
    Your Street Address Here<br>
    Harlow Springs, Arizona 85700<br>
    P (520) 555-0134<br>
    E brian@kolmer-law.example<br>
    W www.kolmer-law.example
  </div>

  <div class="brand">
    <span class="brand__mark"></span>
    <span class="brand__name">Law Office of<br>Brian Kolmer, PLLC</span>
  </div>

  <div class="letterhead__body">
    <p class="recipient">Ms. Jane Roe<br>President<br>Northgate Accountants<br>240 Harbor Lane<br>Riverton, 12345</p>
    <p class="salutation">Dear :</p>
    <p class="paragraph">Lorem ipsum dolor sit amet, consectetur adipiscing elit. Aenean ut ipsum eget massa hendrerit vestibulum vel in velit. Donec pretium neque velit. Vivamus non est turpis, et cursus sem. Mauris vehicula aliquam porta lectus nec mauris ornare venenatis. Vestibulum iaculis pretium placerat. Integer erat in diam auctor at bibendum est lacinia. Morbi imperdiet neque vehicula nunc convallis gravida, nibh nibh varius orci, eget dapibus arcu dui non purus. Pellentesque consequat, est sit amet facilisis eleifend, nibh nulla condimentum a, pulvinar vel lacus. Mauris et molestie nibh in magna mauris. Duis enim sapien, dictum vitae condimentum posuere sit amet interdum elit. Nulla sollicitudin neque eu nulla vestibulum vitae nulla at metus elementum porta.</p>
    <p class="paragraph">Etiam pellentesque, velit id dapibus fermentum, turpis sapien ornare dui, ac tincidunt ligula odio congue purus. Nunc sed ante dui, in porta lectus. Cras nec sem lorem. In hac habitasse platea dictumst. Maecenas id diam quis dui porta tristique. Sed id egestas felis. Donec ullamcorper mattis posuere. Phasellus fermentum eleifend tortor vel dapibus. Vestibulum ante ipsum.</p>
    <div class="signature" role="img" aria-label="Handwritten signature"></div>
    <p>Sincerely,</p>
  </div>
</article>

<section class="card card--upper">
  <div class="brand">
    <span class="brand__mark"></span>
    <span class="brand__name">Law Office of<br>Brian Kolmer, PLLC</span>
  </div>
  <div class="card__rule"></div>
  <div class="card__details">
    <p class="card__title">Brian Kolmer | <span class="role">Criminal Defense Lawyer</span></p>
    <p class="card__line">Your Street Address Here, Harlow Springs, Arizona 85700</p>
    <p class="card__line">P (520) 555-0134 | F (520) 555-0135</p>
    <p class="card__line">brian@kolmer-law.example | www.kolmer-law.example</p>
  </div>
</section>

<section class="card card--lower">
  <div class="brand">
    <span class="brand__mark"></span>
    <span class="brand__name">Law Office of<br>Brian Kolmer, PLLC</span>
  </div>
  <div class="card__rule"></div>
  <div class="card__details">
    <p class="card__title">Brian Kolmer | <span class="role">Criminal Defense Lawyer</span></p>
    <p class="card__line">Your Street Address Here, Harlow Springs, Arizona 85700</p>
    <p class="card__line">P (520) 555-0134 | F (520) 555-0135</p>
    <p class="card__line">brian@kolmer-law.example | www.kolmer-law.example</p>
  </div>
</section>

</body>
</html>
```